Online-Marketing Material für Onlineshop für nachhaltiges Hundezubehör
Zielgruppe
Wir sind ein onlineshop für nachhaltiges Hundezubehör und sind auf der Suche nach einem Banner für unsere Startseite
Aufgabenstellung
wir bieten viele produkte an die aus upgecycelten kletterseilen hergestellt werden(Hundeleinen, Halsbänder, Spielzeug)
das banner soll die nachhaltigkeit unseres hundeshops hervorheben und vertrauen beim kunden generieren.
Vielleicht auch etwas wo der Positive Aspekt des upcyclings auf unsere Erde(weniger Plastik) hervorgehoben wird.
Auf jeden Fall muss(mindestens) ein Hund auf dem Banner zu sehen sein und man muss den Bezug zu Nachhaltigkeit herstellen könen.
Was slogans angeht sind euch natürlich auch keine grenzen gesetzt, umso kreativer, umso besser :)
Das Banner brauche ich in den Maßen 1920x500 , 1280x1000 und 1280x2000

```html
<!DOCTYPE html>
<html lang="de">
<head>
<meta charset="utf-8">
<title>Banner – Wir sorgen für die Erde</title>
<link rel="stylesheet" href="https://fonts.googleapis.com/css2?family=Source+Sans+3:ital,wght@0,400;0,700;1,700&display=swap">
<style>
  :root {
    --green: #78a22f;
    --navy: #0f2d4b;
    --text: #1b3550;
    --white: #ffffff;
    --page: #ffffff;
    --dog-warm: #b98a5e;
    --dog-dark: #4a4644;
    --dog-light: #e9e2da;
    --prod-kraft: #c9a277;
    --prod-pink: #e5b3ac;
    --prod-rope: #d9905a;
    --prod-blue: #6fa6d8;
  }
  * { box-sizing: border-box; margin: 0; padding: 0; }
  html, body { width: 938px; height: 1200px; overflow: hidden; background: var(--page); }
  body { position: relative; font-family: "Source Sans 3", "Source Sans Pro", sans-serif; color: var(--text); }

  .banner {
    position: absolute;
    background: var(--white);
    box-shadow: 0 1px 6px rgba(0,0,0,0.14);
    overflow: hidden;
  }
  .banner--square { left: 47px; top: 138px; width: 411px; height: 317px; }
  .banner--tall   { left: 482px; top: 138px; width: 410px; height: 633px; }
  .banner--wide   { left: 47px; top: 831px; width: 847px; height: 217px; }

  .headline { position: absolute; font-weight: 700; line-height: 1.1; color: var(--green); white-space: nowrap; }
  .headline .accent { color: var(--navy); }

  .copy { position: absolute; font-weight: 400; color: var(--text); white-space: nowrap; }
  .copy strong { color: var(--green); font-weight: 700; }

  .photo-dogs {
    position: absolute;
    background: linear-gradient(90deg, var(--dog-warm) 0%, var(--dog-dark) 30%, var(--dog-light) 58%, var(--dog-warm) 72%, var(--dog-dark) 100%);
    border-radius: 40% 40% 4px 4px / 60% 60% 4px 4px;
    opacity: 0.85;
  }
  .photo-products {
    position: absolute;
    background: linear-gradient(100deg, var(--prod-kraft) 0%, var(--prod-pink) 45%, var(--prod-rope) 80%, var(--prod-blue) 100%);
    border-radius: 8px;
    opacity: 0.85;
  }

  .cta-band { position: absolute; left: 0; right: 0; bottom: 0; }
  .cta-band__tag, .cta-band__shop {
    position: absolute; top: 0; bottom: 0;
    display: flex; align-items: center; justify-content: center;
    font-weight: 700; font-style: italic; color: var(--white); white-space: nowrap;
  }
  .cta-band__tag { left: 0; background: var(--green); }
  .cta-band__shop { right: 0; background: var(--navy); clip-path: polygon(8px 0, 100% 0, 100% 100%, 0 100%); }

  /* square */
  .banner--square .headline { left: 0; right: 0; top: 34px; text-align: center; font-size: 29px; padding-left: 20px; }
  .banner--square .photo-dogs { left: 20px; top: 100px; width: 368px; height: 77px; }
  .banner--square .copy { left: 21px; top: 194px; font-size: 10.8px; line-height: 16px; }
  .banner--square .photo-products { left: 252px; top: 180px; width: 143px; height: 90px; }
  .banner--square .cta-band { height: 36px; }
  .banner--square .cta-band__tag { width: 270px; font-size: 15px; }
  .banner--square .cta-band__shop { width: 149px; font-size: 15px; }

  /* tall */
  .banner--tall .headline { left: 0; right: 0; top: 38px; text-align: center; font-size: 49px; line-height: 59px; }
  .banner--tall .photo-dogs { left: 0; top: 202px; width: 410px; height: 100px; }
  .banner--tall .copy { left: 0; right: 0; top: 320px; text-align: center; font-size: 17.5px; line-height: 25.5px; }
  .banner--tall .photo-products { left: 116px; top: 440px; width: 201px; height: 130px; }
  .banner--tall .cta-band { height: 38px; }
  .banner--tall .cta-band__tag { width: 275px; font-size: 16.5px; }
  .banner--tall .cta-band__shop { width: 144px; font-size: 16.5px; }

  /* wide */
  .banner--wide .headline { left: 58px; top: 18px; font-size: 34px; }
  .banner--wide .photo-dogs { left: 19px; top: 92px; width: 416px; height: 80px; }
  .banner--wide .copy { left: 468px; top: 22px; font-size: 16px; line-height: 24px; }
  .banner--wide .cta-band { height: 36px; }
  .banner--wide .cta-band__tag { width: 424px; font-size: 17px; }
  .banner--wide .cta-band__shop { width: 430px; font-size: 17px; justify-content: flex-start; padding-left: 62px; }
  .banner--wide .photo-products { left: 676px; top: 104px; width: 157px; height: 103px; z-index: 2; }
</style>
</head>
<body>

<section class="banner banner--square">
  <h2 class="headline">Wir sorgen für <span class="accent">die Erde</span></h2>
  <div class="photo-dogs" role="img" aria-label="Vier Hunde schauen über eine Kante"></div>
  <p class="copy">Unserer Produkte darauf, dass durch <strong>Upcycling</strong><br>und <strong>Recycling</strong> so wenig neues Plastik entsteht<br>wie möglich!. Unsere Produkte sind außerdem<br>vegan und frei von Tierleid.</p>
  <div class="photo-products" role="img" aria-label="Produkte: Kotbeutel-Box, Snack-Tüte, Seil-Leine und Halsband"></div>
  <div class="cta-band">
    <span class="cta-band__tag">#JoinOurGreenMovement</span>
    <span class="cta-band__shop">Jetzt einkaufen</span>
  </div>
</section>

<section class="banner banner--tall">
  <h2 class="headline">Wir sorgen für<br><span class="accent">die Erde</span></h2>
  <div class="photo-dogs" role="img" aria-label="Vier Hunde schauen über eine Kante"></div>
  <p class="copy">Unserer Produkte darauf, dass durch <strong>Upcycling</strong><br>und <strong>Recycling</strong> so wenig neues Plastik entsteht<br>wie möglich!. Unsere Produkte sind außerdem<br>vegan und frei von Tierleid.</p>
  <div class="photo-products" role="img" aria-label="Produkte: Kotbeutel-Box, Snack-Tüte, Seil-Leine und Halsband"></div>
  <div class="cta-band">
    <span class="cta-band__tag">#JoinOurGreenMovement</span>
    <span class="cta-band__shop">Jetzt einkaufen</span>
  </div>
</section>

<section class="banner banner--wide">
  <h2 class="headline">Wir sorgen für <span class="accent">die Erde</span></h2>
  <div class="photo-dogs" role="img" aria-label="Vier Hunde schauen über eine Kante"></div>
  <p class="copy">Unserer Produkte darauf, dass durch <strong>Upcycling</strong><br>und <strong>Recycling</strong> so wenig neues Plastik entsteht<br>wie möglich!. Unsere Produkte sind außerdem<br>vegan und frei von Tierleid.</p>
  <div class="cta-band">
    <span class="cta-band__tag">#JoinOurGreenMovement</span>
    <span class="cta-band__shop">Jetzt einkaufen</span>
  </div>
  <div class="photo-products" role="img" aria-label="Produkte: Kotbeutel-Box, Snack-Tüte, Seil-Leine und Halsband"></div>
</section>

</body>
</html>
```